Fun, Clean Business Card For Family Focused Travel Agency

I need a business card using specific colors and fonts as in the uploaded files. Ideally, I would like a large image of the logo on the back and all the contact info on the front. Maybe the stars/dots somewhere in a flowy form.

I do want it the contact information to be clear and easy to read. I don't want it to look too busy. Maybe even a bit minimalist.

I plan or ordering the ROUNDED CORNER business cards from Cardwell Press, so please consider that in your design.

Target Market(s)

Families with children, couples, groups of friends

Contact Information for Business Card

Marla Quent, Owner
Marla@TidewayTrips.example
Cell Phone Number 555-218-6034
Office Phone Number 555-647-1295
Specializing in Fablecrest destinations, Goldmere Parkside Resort, Cruises and All-Inclusive Vacations.

Nice but not required:
www.TidewayTrips.example
Facebook, Instagram, Twitter icons with username: TidewayTrips

Font styles to use
Sans Serif

Requirements
Must have
• Please try to use the colors from the logo as much as possible. I understand lighter shades/colors may be needed for some things.
Should not have
• NO SERIF FONTS. That is really the only thing I do not want at all

```html
<!DOCTYPE html>
<html lang="en">
<head>
<meta charset="utf-8">
<title>Tideway Trips – Business Card</title>
<link rel="stylesheet" href="https://fonts.googleapis.com/css2?family=Open+Sans:wght@400;600;700&display=swap">
<style>
  :root{
    --navy:#14152b;
    --orange:#ee7623;
    --teal:#1ea68b;
    --blue:#1b8fd6;
    --green:#8cc63f;
    --yellow:#d6b32c;
    --ink:#1d1d2b;
    --paper:#ffffff;
    --backdrop:#e9ebed;
  }
  *{box-sizing:border-box;margin:0;padding:0}
  html,body{width:1200px;height:900px;overflow:hidden}
  body{background:var(--backdrop);font-family:"Open Sans",Arial,sans-serif;position:relative}

  .card{position:absolute;left:285px;width:630px;height:360px;border-radius:16px;overflow:hidden;box-shadow:0 6px 18px rgba(0,0,0,.12)}
  .card--back{top:45px;background:var(--navy)}
  .card--front{top:495px;background:var(--paper)}

  .band{position:absolute;height:20px;background:var(--orange)}
  .band--top{top:0;left:80px;width:300px}
  .band--bottom{bottom:0;left:300px;width:270px}

  .wordmark{position:absolute;display:flex;align-items:center;gap:14px;font-weight:700;white-space:nowrap}
  .wordmark__dot{border-radius:50%;background:var(--teal);flex:none}
  .card--back .wordmark{left:120px;top:120px;font-size:54px;color:#fff}
  .card--back .wordmark__dot{width:34px;height:34px}
  .card--front .wordmark{left:62px;top:102px;font-size:40px;color:var(--ink)}
  .card--front .wordmark__dot{width:26px;height:26px}

  .tagline{position:absolute;left:0;right:0;top:228px;text-align:center;color:var(--orange);font-weight:700;font-size:15px;line-height:1.45}

  .decor{position:absolute;inset:0;pointer-events:none}

  .person{position:absolute;right:70px;top:60px;text-align:right}
  .person__name{font-size:18px;letter-spacing:.5px;color:var(--ink);padding-bottom:4px;border-bottom:1px solid var(--blue)}
  .person__first{color:var(--teal)}
  .person__role{font-size:14px;font-weight:600;color:var(--ink);margin-top:3px}

  .rule{position:absolute;left:62px;top:185px;width:390px;height:1px;background:var(--orange)}

  .contacts{position:absolute;left:62px;top:205px;list-style:none}
  .contacts li{display:flex;align-items:center;gap:10px;font-size:15px;color:var(--ink);height:29px}
  .contacts .accent{color:var(--teal)}
  .icon{width:20px;height:20px;border-radius:50%;display:flex;align-items:center;justify-content:center;flex:none}
  .icon--teal{background:var(--teal)}
  .icon--orange{background:var(--orange)}
  .icon--green{background:var(--green)}
  .icon--yellow{background:var(--yellow)}
</style>
</head>
<body>

<section class="card card--back" aria-label="Card back">
  <div class="band band--top"></div>
  <div class="band band--bottom"></div>
  <svg class="decor" viewBox="0 0 630 360" aria-hidden="true">
    <circle cx="100" cy="112" r="3" fill="var(--orange)"/>
    <circle cx="88" cy="150" r="2.5" fill="var(--green)"/>
    <circle cx="112" cy="200" r="3" fill="var(--blue)"/>
    <circle cx="78" cy="185" r="2" fill="var(--yellow)"/>
    <path d="M130 95l2 5 5 2-5 2-2 5-2-5-5-2 5-2z" fill="var(--blue)"/>
    <path d="M95 135l1.5 3.5 3.5 1.5-3.5 1.5-1.5 3.5-1.5-3.5-3.5-1.5 3.5-1.5z" fill="var(--teal)"/>
    <circle cx="520" cy="105" r="2.5" fill="var(--yellow)"/>
    <circle cx="560" cy="100" r="3" fill="var(--teal)"/>
  </svg>
  <div class="wordmark"><span class="wordmark__dot"></span>Tideway Trips</div>
  <p class="tagline">Specializing in Fablecrest destinations, Goldmere Parkside Resort<br>Cruises and All-Inclusive Vacations</p>
</section>

<section class="card card--front" aria-label="Card front">
  <div class="band band--top"></div>
  <div class="band band--bottom"></div>
  <svg class="decor" viewBox="0 0 630 360" aria-hidden="true">
    <circle cx="405" cy="42" r="7" fill="var(--orange)"/>
    <circle cx="250" cy="66" r="7" fill="var(--orange)"/>
    <circle cx="585" cy="160" r="5" fill="var(--orange)"/>
    <path d="M395 12l2.5 6 6 2.5-6 2.5-2.5 6-2.5-6-6-2.5 6-2.5z" fill="var(--blue)"/>
    <path d="M478 158l2.5 6 6 2.5-6 2.5-2.5 6-2.5-6-6-2.5 6-2.5z" fill="var(--blue)"/>
    <path d="M595 34l1.5 3.5 3.5 1.5-3.5 1.5-1.5 3.5-1.5-3.5-3.5-1.5 3.5-1.5z" fill="var(--green)"/>
    <path d="M420 150l1.5 3.5 3.5 1.5-3.5 1.5-1.5 3.5-1.5-3.5-3.5-1.5 3.5-1.5z" fill="var(--green)"/>
    <circle cx="460" cy="34" r="2.5" fill="var(--green)"/>
    <circle cx="520" cy="205" r="4" fill="var(--yellow)"/>
    <circle cx="560" cy="235" r="3" fill="var(--blue)"/>
    <circle cx="602" cy="118" r="2.5" fill="var(--blue)"/>
    <circle cx="48" cy="92" r="2.5" fill="var(--orange)"/>
  </svg>

  <div class="person">
    <p class="person__name"><span class="person__first">MARLA</span> QUENT</p>
    <p class="person__role">Owner</p>
  </div>

  <div class="wordmark"><span class="wordmark__dot"></span>Tideway Trips</div>
  <div class="rule"></div>

  <ul class="contacts">
    <li><span class="icon icon--teal"><svg width="10" height="12" viewBox="0 0 10 12"><rect x="1.5" y="0.5" width="7" height="11" rx="1.5" fill="none" stroke="#fff" stroke-width="1.3"/><circle cx="5" cy="9.3" r=".9" fill="#fff"/></svg></span>555 218 6034</li>
    <li><span class="icon icon--orange"><svg width="12" height="12" viewBox="0 0 24 24"><path d="M6.6 10.8a15 15 0 006.6 6.6l2.2-2.2a1 1 0 011-.25 11 11 0 003.6.6 1 1 0 011 1V20a1 1 0 01-1 1A17 17 0 013 4a1 1 0 011-1h3.5a1 1 0 011 1c0 1.250.2 2.450.6 3.6a1 1 0 01-.25 1z" fill="#fff"/></svg></span>555 647 1295</li>
    <li><span class="icon icon--green"><svg width="12" height="9" viewBox="0 0 12 9"><rect x=".6" y=".6" width="10.8" height="7.8" rx="1" fill="none" stroke="#fff" stroke-width="1.2"/><path d="M.8 1l5.2 4 5.2-4" fill="none" stroke="#fff" stroke-width="1.2"/></svg></span>Marla@TidewayTrips.example</li>
    <li><span class="icon icon--yellow"><svg width="12" height="12" viewBox="0 0 12 12"><circle cx="6" cy="6" r="5" fill="none" stroke="#fff" stroke-width="1.1"/><ellipse cx="6" cy="6" rx="2.2" ry="5" fill="none" stroke="#fff" stroke-width="1"/><path d="M1 6h10" stroke="#fff" stroke-width="1"/></svg></span><span>www.<span class="accent">TidewayTrips</span>.example</span></li>
  </ul>
</section>

</body>
</html>
```